Need a business card portraying store logo and up and coming business of quilt fabrics, apparel fabrics, notions and buttons. Our business name is Larkspur Quilt Studio. Am attaching logo. The design should communicate a growing business and warm atmosphere. Would like address and store hours and contact info displayed on card. Mon - Fri 9:30 to 5:00, Saturday 9:30 to 1:00. Address 238 W Elm Ave, Ashby, OR 97392 email: larkspurquiltstudio@mailbarn.net. Phone and fax 541-555-2847. After hours contact # 458-555-3916 Also like vintage sewing machines and dress forms if it works to incorporate fine, if not thats ok too.

```html
<!DOCTYPE html>
<html lang="en">
<head>
<meta charset="utf-8">
<title>Larkspur Quilt Studio — Business Card</title>
<link rel="stylesheet" href="https://fonts.googleapis.com/css2?family=Arimo:wght@400;700&display=swap">
<style>
  :root {
    --backdrop: #dcdcdc;
    --card: #ffffff;
    --ink: #1c1c1c;
    --brand-red: #9e1218;
    --accent-deep: #7a0e13;
    --accent-light: #b3222a;
    --stitch: #8a1a1f;
  }
  * { margin: 0; padding: 0; box-sizing: border-box; }
  html, body {
    width: 1200px;
    height: 675px;
    overflow: hidden;
    background: var(--backdrop);
    font-family: "Arimo", Arial, sans-serif;
    color: var(--ink);
  }
  .card {
    position: absolute;
    top: 189px;
    width: 520px;
    height: 297px;
    background: var(--card);
    overflow: hidden;
    box-shadow: 0 6px 18px rgba(0,0,0,0.18);
  }
  .card--front { left: 50px; }
  .card--back { left: 630px; }

  .brand__name {
    font-size: 19px;
    font-weight: 400;
    color: var(--brand-red);
    white-space: nowrap;
  }
  .card--front .brand {
    position: absolute;
    top: 26px;
    left: 26px;
  }

  .corner-art {
    position: absolute;
    top: 0;
    right: 0;
    width: 170px;
    height: 170px;
    background: linear-gradient(225deg, var(--accent-light), var(--accent-deep));
  }

  .contact {
    position: absolute;
    top: 92px;
    left: 26px;
    list-style: none;
    font-size: 14px;
    line-height: 22px;
  }
  .contact__item {
    display: flex;
    align-items: center;
    gap: 6px;
  }
  .contact__icon {
    width: 12px;
    height: 12px;
    flex: none;
  }

  .hours {
    position: absolute;
    bottom: 30px;
    left: 250px;
    display: flex;
    gap: 52px;
    font-size: 15px;
    font-weight: 700;
    line-height: 20px;
  }
  .hours__day { display: block; }

  .card--back .stitch-frame {
    position: absolute;
    inset: 14px;
    border: 1.5px dashed var(--stitch);
  }
  .card--back .brand {
    position: absolute;
    top: 50%;
    left: 50%;
    transform: translate(-50%, -50%);
  }
  .card--back .brand__name { font-size: 24px; }
</style>
</head>
<body>

<section class="card card--front" aria-label="Business card front">
  <div class="corner-art" role="img" aria-label="Decorative red sewing notion illustration"></div>

  <div class="brand">
    <span class="brand__name">Larkspur Quilt Studio</span>
  </div>

  <ul class="contact">
    <li class="contact__item">238 W Elm Ave, Ashby, OR 97392</li>
    <li class="contact__item">
      <svg class="contact__icon" viewBox="0 0 12 12" aria-hidden="true">
        <rect x="0.5" y="2" width="11" height="8" fill="none" stroke="#9e1218" stroke-width="1.3"/>
        <path d="M1 2.5 L6 6.5 L11 2.5" fill="none" stroke="#9e1218" stroke-width="1.3"/>
      </svg>
      larkspurquiltstudio@mailbarn.net
    </li>
    <li class="contact__item">
      <svg class="contact__icon" viewBox="0 0 12 12" aria-hidden="true">
        <path d="M2.5 1 L4.5 1 L5.2 3.6 L4 4.6 Q5 7 7.4 8 L8.4 6.8 L11 7.5 L11 9.5 Q11 11 9.5 11 Q1 10 1 2.5 Q1 1 2.5 1 Z" fill="#9e1218"/>
      </svg>
      541-555-2847
    </li>
    <li class="contact__item">After hours contact # 458-555-3916</li>
  </ul>

  <div class="hours">
    <p><span class="hours__day">Mon - Fri</span>9:30 to 5:00</p>
    <p><span class="hours__day">Saturday</span>9:30 to 1:00</p>
  </div>
</section>

<section class="card card--back" aria-label="Business card back">
  <div class="stitch-frame"></div>
  <div class="brand">
    <span class="brand__name">Larkspur Quilt Studio</span>
  </div>
</section>

</body>
</html>
```